Honey Company from Florida Needs Sweet and Buzz-worthy Site

Website Requests:
-Deluxe 5-Page Website with SSL-Secure Online Store (Shopify)
-High-end imagery to appeal to a discerning consumer
-Detailed verbiage with strong SEO and easy readability
-Design principles: simple, chic, luxe, earthy
Pages:
1. Home {Local, Raw American Honey from Florida}
2. The Hive
> About Us
>Meet the Beekeepers
3. Buy Honey
> Shopify retail store
4. The Buzz {News, Recipes & More}
> Blog
5. Contact Us {We're Buzzin' to Meet You}
> Store Hours
> Phone Number
> Address
> Quick Contact Form
Target Market(s)
High-end honey consumer in the U.S.
Industry/Entity Type
Upscale honey enthusiasts; direct to consumer sales.
Coding
Coded - Design and coding required
Number of Pages Required
5+ page
Requirements
Must have
- Upscale look and feel, easy usability for quick sales.

```html
<!DOCTYPE html>
<html lang="en">
<head>
<meta charset="utf-8">
<title>Golden Comb Company — Raw Florida Honey</title>
<link href="https://fonts.googleapis.com/css2?family=Roboto+Slab:wght@700;800&family=Roboto:ital,wght@0,400;0,500;1,400&family=Roboto+Condensed:ital,wght@1,400&display=swap" rel="stylesheet">
<style>
:root{
  --gold:#ecc452;
  --ink:#1d1d1f;
  --text:#555558;
  --hero:#3e3f42;
  --footer:#1f1f23;
  --white:#ffffff;
}
*{margin:0;padding:0;box-sizing:border-box}
html,body{width:1200px;height:3769px;overflow:hidden;background:var(--white)}
body{position:relative;font-family:"Roboto",Arial,sans-serif;color:var(--text)}
.abs{position:absolute}
.slab{font-family:"Roboto Slab",Georgia,serif}

/* header */
.brand{left:143px;top:6px;width:140px;height:140px;border:2px solid var(--ink);border-radius:50%;display:flex;align-items:center;justify-content:center;text-align:center;font-family:"Roboto Slab",serif;font-weight:700;font-size:19px;line-height:1.1;color:var(--ink)}
.nav{left:440px;top:62px;display:flex;gap:33px;font-family:"Roboto Slab",serif;font-weight:700;font-size:16px;color:var(--ink)}
.nav a{color:inherit;text-decoration:none;padding-bottom:6px}
.nav a.active{border-bottom:3px solid var(--gold)}
.icons{left:1005px;top:64px;display:flex;gap:18px}

/* hero */
.hero{left:0;top:148px;width:1200px;height:564px;background:linear-gradient(100deg,#36373a 0%,#3f4043 45%,#5a5a5a 70%,#3a3b3e 100%)}
.hero-title{left:0;top:286px;width:1200px;text-align:center;font-family:"Roboto Slab",serif;font-weight:800;font-size:50px;line-height:61px;color:var(--white);letter-spacing:1px}

.btn{display:flex;align-items:center;justify-content:center;background:var(--gold);color:var(--ink);font-family:"Roboto Slab",serif;font-weight:700;font-size:14px;letter-spacing:.5px}

.photo{background:linear-gradient(135deg,#26262a 0%,#3a3424 55%,#c9a03a 100%)}
.photo.light{background:linear-gradient(160deg,#f1ede6 0%,#d8b878 55%,#8a5a22 100%)}

h2{position:absolute;font-family:"Roboto Slab",serif;font-weight:800;font-size:50px;line-height:61px;color:var(--ink);letter-spacing:1px}
.copy{position:absolute;font-size:13px;line-height:24.8px;color:var(--text)}

/* products */
.product{position:absolute;top:1449px;width:213px}
.product .thumb{width:213px;height:213px}
.product .name{margin-top:24px;text-align:center;font-family:"Roboto Slab",serif;font-weight:700;font-size:14px;color:var(--ink)}
.product .price{margin-top:9px;text-align:center;font-family:"Roboto Slab",serif;font-weight:700;font-size:13px;color:var(--gold)}

/* quote band */
.band{left:0;top:2355px;width:1200px;height:295px;background:var(--gold)}
.band-quote{left:0;top:2448px;width:1200px;text-align:center;font-family:"Roboto Condensed",sans-serif;font-style:italic;font-size:35px;line-height:49px;color:var(--white)}
.pull{position:absolute;top:2718px;width:420px;text-align:center;font-style:italic;font-size:12px;line-height:26px;color:var(--text)}

/* footer */
.footer{left:0;top:3437px;width:1200px;height:332px;background:var(--footer)}
.foot-head{position:absolute;top:3490px;font-family:"Roboto",sans-serif;font-weight:500;font-size:18px;color:var(--gold)}
.foot-text{position:absolute;font-size:13px;color:var(--white)}
.email{left:609px;top:3542px;width:297px;height:54px;background:var(--white);padding-left:38px;display:flex;align-items:center;font-family:"Roboto Slab",serif;font-weight:700;font-size:11px;color:var(--ink)}
.pay{position:absolute;top:3688px;display:flex;gap:12px}
.pay span{width:31px;height:20px;border-radius:2px;background:#d9d9dc}
.social{position:absolute;top:3686px;left:450px;display:flex;gap:17px}
.social span{width:24px;height:24px;border-radius:3px;background:var(--white)}
</style>
</head>
<body>

<header>
  <div class="abs brand">Golden<br>Comb<br>Company</div>
  <nav class="abs nav">
    <a class="active" href="#">Home</a>
    <a href="#">The Hive</a>
    <a href="#">Buy Honey</a>
    <a href="#">The Buzz</a>
    <a href="#">Contact Us</a>
  </nav>
  <div class="abs icons">
    <svg width="16" height="16" viewBox="0 0 16 16" aria-label="Search"><circle cx="6.5" cy="6.5" r="4.5" fill="none" stroke="#1d1d1f" stroke-width="2"/><line x1="10" y1="10" x2="14" y2="14" stroke="#1d1d1f" stroke-width="2"/></svg>
    <svg width="14" height="16" viewBox="0 0 14 16" aria-label="Cart"><path d="M4 5V3a3 3 0 0 1 6 0v2" fill="none" stroke="#1d1d1f" stroke-width="1.6"/><rect x="1" y="5" width="12" height="10" fill="#1d1d1f"/></svg>
  </div>
</header>

<section>
  <div class="abs hero" role="img" aria-label="Honey jar beside an open gift box with bees on a dark backdrop"></div>
  <div class="abs hero-title">STRAIGHT FROM OUR<br>BELOVED HIVES TO<br>YOUR LOVELY HOME</div>
  <div class="abs btn" style="left:507px;top:503px;width:185px;height:59px">GOES HERE</div>
</section>

<section>
  <div class="abs photo" style="left:143px;top:782px;width:394px;height:432px" role="img" aria-label="Black gift box holding honey jars and wooden spoons"></div>
  <h2 style="left:619px;top:808px">DESCRIPTION</h2>
  <p class="copy" style="left:619px;top:888px;width:440px">100% raw, unfiltered Florida honey straight from he beehives on his six-acre property, Golden Comb Honey Farm, 1480 Orchard Lane, Clearwater Springs. Agricultural Company specializing in the Production of 100% Raw American Honey, and the Pollination of America's food crops. Our Honey comes straight from our beehives to your table. No filtering, heating, or any funny stuff. Just All Natural, 100% Pure Florida Honey Natural Wild Honey- flavors include Orange Blossom, Gallberry, Summer Wildflower, Winter Wildflower, and many more.</p>
  <div class="abs btn" style="left:620px;top:1123px;width:150px;height:54px">READ MORE</div>
</section>

<section>
  <h2 style="left:0;top:1335px;width:1200px;text-align:center">FEATURED PRODUCTS</h2>
  <div class="product" style="left:145px"><div class="thumb photo light" role="img" aria-label="Hexagonal honey boxes stacked"></div><div class="name">PRODUCT NAME</div><div class="price">$56.77</div></div>
  <div class="product" style="left:377px"><div class="thumb photo light" role="img" aria-label="Three honey bottles with a wooden dipper"></div><div class="name">PRODUCT NAME</div><div class="price">$56.77</div></div>
  <div class="product" style="left:609px"><div class="thumb photo light" role="img" aria-label="Honey bottle in a honeycomb wooden case"></div><div class="name">PRODUCT NAME</div><div class="price">$56.77</div></div>
  <div class="product" style="left:843px"><div class="thumb photo" role="img" aria-label="Honey jars in a black gift box"></div><div class="name">PRODUCT NAME</div><div class="price">$56.77</div></div>
</section>

<section>
  <h2 style="left:143px;top:1855px">IMPORTANCE<br>OF BEES</h2>
  <p class="copy" style="left:143px;top:1990px;width:450px">They are very misunderstood among the public. We have lost a great amount of our natural forage land due to urbanization and suburban sprawl, and when people and honeybees mix, it's going to have less than desirable results. I receive complaints about my bees going to neighbors' swimming pools to gather fresh water to swarms of bees moving into people's property. You name it, I've dealt with it. But it takes patience and mutual understanding on both sides to overcome the obstacles</p>
  <div class="abs btn" style="left:145px;top:2195px;width:149px;height:54px">READ MORE</div>
  <div class="abs photo light" style="left:665px;top:1842px;width:393px;height:431px" role="img" aria-label="Kraft gift box with three honey bottles and a dipper"></div>
</section>

<section>
  <div class="abs band"></div>
  <p class="abs band-quote">“If the bee disappeared off the face of the Earth, man would<br>have only four years left to live.”</p>
  <p class="pull" style="left:151px">“Over one-third of our entire diet is dependent on pollination from the honeybee. So, for every three bites of food you eat,you can thank the honeybee for one of those three bites,” Marlow says.</p>
  <p class="pull" style="left:624px">“Without beekeepers and the pollination services their hives provide to growers in the U.S., we would lose a significant yield from many crops, including blueberries, watermelons, zucchinis, and almonds, to name a few, which would cause food prices to rise as the supply would diminish,</p>
</section>

<section>
  <div class="abs photo" style="left:143px;top:2909px;width:394px;height:431px" role="img" aria-label="Black gift box holding honey jars and wooden spoons"></div>
  <h2 style="left:619px;top:2911px">THE HEALTH<br>BENEFITS OF<br>HONEY</h2>
  <p class="copy" style="left:619px;top:3111px;width:440px">“Real Local Honey, Really Good for You”<br>Raw honey is loaded with antioxidants to protect your body from cell damage due to free radicals. Honey has been long<br>known as a folk remedy to help heal burns and wounds due to its antibacterial and antifungal properties.</p>
  <div class="abs btn" style="left:620px;top:3300px;width:150px;height:54px">READ MORE</div>
</section>

<footer>
  <div class="abs footer"></div>
  <div class="foot-head" style="left:143px">CONTACT INFO</div>
  <div class="foot-text" style="left:143px;top:3541px">(555) 014-2290 | 1480 Orchard Lane, Clearwater Springs, FL 34000</div>
  <div class="foot-head" style="left:609px">SIGN-UP FOR OUR EMAILS</div>
  <div class="abs email">ENTER EMAIL</div>
  <div class="abs btn" style="left:906px;top:3542px;width:149px;height:54px">SIGN UP</div>
  <div class="pay" style="left:143px" aria-label="Accepted payment methods"><span></span><span></span><span></span><span></span><span></span></div>
  <div class="social" aria-label="Social links"><span></span><span></span></div>
  <div class="foot-text" style="right:145px;top:3690px">© 2021 Golden Comb.All Rights reserved &nbsp;| &nbsp;Privacy policy &nbsp;| &nbsp;Terms and Use</div>
</footer>

</body>
</html>
```